A clean crisp business card for a Landscape Construction company. Designed to be easy to read contact/ info and also be appealing/interesting, unlike a traditional business card.

Industry/Entity Type

Landscape Construction

Contact Information for Business Card

Company name : Bramblecrest Landscape Construction, phone number: (877) 62Vales, website:Bramblecrestlandscapes.example, Email, sales@bramblecrestlandscapes.example

Requirements
Nice to have
• Luxurious finishes/ details…. Icons or emblems next to contact info
Should not have
• Clipart or general pictures

```html
<!DOCTYPE html>
<html lang="en">
<head>
<meta charset="UTF-8">
<title>Bramblecrest Landscape Construction – Business Card</title>
<link rel="stylesheet" href="https://fonts.googleapis.com/css2?family=Poppins:wght@400;500&display=swap">
<style>
  :root {
    --page-bg: #ffffff;
    --card-bg: #ffffff;
    --brand-blue: #2a6db8;
    --brand-green: #8cc63f;
    --text-blue: #2d6cb5;
  }
  * { margin: 0; padding: 0; box-sizing: border-box; }
  html, body {
    width: 1200px;
    height: 1000px;
    overflow: hidden;
    background: var(--page-bg);
  }
  .canvas {
    position: relative;
    width: 1200px;
    height: 1000px;
  }
  .business-card {
    position: absolute;
    left: 181px;
    top: 262px;
    width: 838px;
    height: 477px;
    background: var(--card-bg);
    border: 1px solid #ececec;
    overflow: hidden;
  }
  .brand {
    position: absolute;
    left: 34px;
    top: 118px;
    width: 352px;
    display: flex;
    flex-direction: column;
    align-items: center;
    font-family: "Poppins", sans-serif;
    font-weight: 500;
    color: var(--brand-blue);
    text-align: center;
  }
  .brand-dot {
    width: 58px;
    height: 58px;
    border-radius: 50%;
    background: var(--brand-green);
    margin-bottom: 18px;
  }
  .brand-name {
    font-size: 40px;
    line-height: 1.05;
    letter-spacing: 0.5px;
  }
  .brand-tagline {
    font-size: 15.5px;
    letter-spacing: 3.4px;
    text-transform: uppercase;
    margin-top: 6px;
  }
  .divider {
    position: absolute;
    left: 417px;
    top: 176px;
    width: 2px;
    height: 163px;
    background: var(--brand-blue);
  }
  .contact-list {
    position: absolute;
    left: 431px;
    top: 218px;
    width: 385px;
    list-style: none;
    font-family: "Poppins", sans-serif;
    font-weight: 400;
    font-size: 17.5px;
    color: var(--text-blue);
  }
  .contact-item {
    display: flex;
    align-items: center;
    height: 30.5px;
    white-space: nowrap;
  }
  .contact-icon {
    width: 20px;
    height: 20px;
    margin-right: 7px;
    flex-shrink: 0;
  }
  .footer-band {
    position: absolute;
    left: 0;
    bottom: 0;
    width: 100%;
    height: 24px;
    background: var(--brand-blue);
  }
</style>
</head>
<body>
<div class="canvas">
  <section class="business-card">
    <div class="brand">
      <div class="brand-dot"></div>
      <div class="brand-name">Bramblecrest</div>
      <div class="brand-tagline">Landscape Construction</div>
    </div>

    <div class="divider"></div>

    <ul class="contact-list">
      <li class="contact-item">
        <svg class="contact-icon" viewBox="0 0 24 24" aria-hidden="true">
          <path fill="#8cc63f" d="M6.6 10.8c1.4 2.8 3.8 5.1 6.6 6.6l2.2-2.2c.3-.3.7-.4 1-.2 1.1.4 2.3.6 3.6.6.6 0 1 .4 1 1V20c0 .6-.4 1-1 1C10.6 21 3 13.4 3 4c0-.6.4-1 1-1h3.5c.6 0 1 .4 1 1 0 1.3.2 2.5.6 3.6.1.3 0 .7-.2 1L6.6 10.8z"/>
        </svg>
        <span>(877) 62Vales</span>
      </li>
      <li class="contact-item">
        <svg class="contact-icon" viewBox="0 0 24 24" aria-hidden="true">
          <rect x="2" y="5" width="20" height="14" rx="1" fill="#8cc63f"/>
          <path d="M2.5 6l9.5 7 9.5-7" fill="none" stroke="#ffffff" stroke-width="1.6"/>
        </svg>
        <span>sales@bramblecrestlandscapes.example</span>
      </li>
      <li class="contact-item">
        <svg class="contact-icon" viewBox="0 0 24 24" aria-hidden="true">
          <circle cx="12" cy="12" r="10" fill="#8cc63f"/>
          <g fill="none" stroke="#ffffff" stroke-width="1.3">
            <ellipse cx="12" cy="12" rx="4.2" ry="10"/>
            <line x1="2" y1="12" x2="22" y2="12"/>
            <line x1="12" y1="2" x2="12" y2="22"/>
            <path d="M4 7h16M4 17h16"/>
          </g>
        </svg>
        <span>Bramblecrestlandscapes.example</span>
      </li>
    </ul>

    <div class="footer-band"></div>
  </section>
</div>
</body>
</html>
```